Business Card Design

Stronger Care Network for the Riverlands is a partnership of twenty different health organisations in the western suburbs of Melbourne, working together to improve the health of the local community. The western suburbs of Melbourne is one of the fastest growing and most culturally diverse populations in Australia and its communities have some of the poorest health outcomes in Australia.
Please see location for copy of the SCNR:
http://qvlr.com.au/fileadmin/filemount/pdf_files/SCNFTR_13_FINAL_JUNE_2012.pdf
Updates

Reason: Hello. I've extended the deadline because in the brief I made a confusing mention about a logo, but I actually meant the 'Stronger Care Network for the Riverlands' jpg that I had already attached. Sorry about the confusion Thanks Rosalind

Hello, Thanks for the designs I have already received. I have extended the deadline because I made a confusing reference to a logo in my brief, but I was talking about the 'Stronger Care Network for the Riverlands' jpg I had already attached. There is no other logo for me to provide.

Thanks, Rosalind

Target Market(s)

Health and state/local government managers and CEOs

Industry/Entity Type

Health

Contact Information for Business Card

Rosalind Tiernan
Executive Officer
Stronger Care Network for the Riverlands
Ph: 0438 295 614
Rosalind.Tiernan@kp.org.au

Requirements
Must have
• logo and details as provided.
Would prefer matt finish
I can't see that logo has successfully attached so if it has not, please email or call me to follow up.

```html
<!DOCTYPE html>
<html lang="en">
<head>
<meta charset="utf-8">
<title>Stronger Care Network for the Riverlands — Business Card</title>
<link rel="stylesheet" href="https://fonts.googleapis.com/css2?family=Mulish:wght@400;500&family=Roboto+Slab:wght@700&display=swap">
<style>
  :root {
    --brand-blue: #0a8bcf;
    --brand-green: #bad764;
    --card-white: #ffffff;
    --ink-dark: #2b2b2b;
    --ink-grey: #505050;
    --ink-soft: #5c5c5c;
    --page-bg: #ffffff;
  }
  * { margin: 0; padding: 0; box-sizing: border-box; }
  html, body {
    width: 1200px; height: 1000px; overflow: hidden;
    background: var(--page-bg);
    font-family: "Mulish", sans-serif;
  }
  .canvas { position: relative; width: 1200px; height: 1000px; }

  .card {
    position: absolute; left: 240px; width: 653px; height: 402px;
    overflow: hidden;
    box-shadow: 0 6px 18px rgba(0,0,0,0.18);
  }
  .card--front { top: 89px; background: var(--card-white); }
  .card--back  { top: 520px; background: var(--brand-blue); }

  .band { position: absolute; top: 0; height: 100%; }
  .card--front .band { left: 43px; width: 174px; background: var(--brand-blue); }
  .card--back .band  { left: 436px; width: 174px; background: var(--brand-green); }

  .wordmark {
    position: absolute;
    color: var(--card-white);
    font-family: "Roboto Slab", serif;
    font-weight: 700;
    letter-spacing: -0.03em;
  }
  .wordmark span { display: block; }
  .wordmark__mark {
    display: block;
    background: var(--brand-green);
  }
  .card--front .wordmark { left: 69px; top: 56px; font-size: 23px; line-height: 30px; }
  .card--front .wordmark__mark { width: 16px; height: 16px; margin-top: 8px; }
  .card--back .wordmark  { left: 138px; top: 96px; font-size: 40px; line-height: 42px; }
  .card--back .wordmark__mark { width: 26px; height: 26px; margin-top: 12px; }

  .contact {
    position: absolute; right: 64px; top: 178px;
    text-align: right;
  }
  .contact__name  { color: var(--brand-blue); font-size: 31px; font-weight: 500; line-height: 38px; }
  .contact__role  { color: var(--ink-dark); font-size: 24px; font-weight: 400; line-height: 32px; }
  .contact__org   { color: var(--ink-grey); font-family: "Roboto Slab", serif; font-size: 16px; font-weight: 700; letter-spacing: -0.01em; line-height: 28px; margin-top: 2px; }
  .contact__email,
  .contact__phone { color: var(--ink-soft); font-size: 17px; font-weight: 400; line-height: 26px; }
  .contact__email { margin-top: 2px; }
</style>
</head>
<body>
<main class="canvas">
  <section class="card card--front" aria-label="Business card front">
    <div class="band"></div>
    <div class="wordmark" aria-label="Stronger Care Network for the Riverlands">
      <span>Stronger</span><span>Care</span><span>Network</span><span>for the</span><span>Riverlands</span>
      <i class="wordmark__mark" aria-hidden="true"></i>
    </div>
    <div class="contact">
      <p class="contact__name">Rosalind Tiernan</p>
      <p class="contact__role">Executive Officer</p>
      <p class="contact__org">Stronger Care Network for the Riverlands</p>
      <p class="contact__email">Rosalind.Tiernan@kp.org.au</p>
      <p class="contact__phone">Ph:&nbsp; 0438 295 614</p>
    </div>
  </section>

  <section class="card card--back" aria-label="Business card back">
    <div class="band"></div>
    <div class="wordmark" aria-label="Stronger Care Network for the Riverlands">
      <span>Stronger</span><span>Care</span><span>Network</span><span>for the</span><span>Riverlands</span>
      <i class="wordmark__mark" aria-hidden="true"></i>
    </div>
  </section>
</main>
</body>
</html>
```